A four page single-fold product brochure

The brochure is for a pair of Industrial products. A four page, single fold, post card size brochure preferably with a dark themed, carbon fiber texture background.

I also want to do a spot varnish pattern on the brochure. The varnish effect maybe applied on the image / logo or some accent lines.

I have attached a word documents with pictures and other detailed instructions. Please feel free to contact me if you have any questions. If the images attached won't work for a dark background, please advise.

Thanks, Good Luck!

Industry/Entity Type

Industrial

Requirements
Must have
• Out of the box, modern, special effects

```html
<!DOCTYPE html>
<html lang="en">
<head>
<meta charset="utf-8">
<title>KT-Transmitter Brochure Spread</title>
<link href="https://fonts.googleapis.com/css2?family=Open+Sans:wght@400;600;700;800&display=swap" rel="stylesheet">
<style>
  :root {
    --backdrop: #ececec;
    --page-black: #0b0b0b;
    --carbon-a: #141414;
    --carbon-b: #0a0a0a;
    --text-light: #e6e6e6;
    --accent-blue: #2aa3d8;
    --accent-green: #2fa65a;
    --cell-light: #f2f2f2;
    --cell-mid: #c9c9c9;
    --cell-head: #8a8a8a;
    --cell-line: #555;
  }
  * { box-sizing: border-box; margin: 0; padding: 0; }
  html, body { width: 1200px; height: 800px; overflow: hidden; }
  body {
    background: var(--backdrop);
    font-family: "Open Sans", Arial, sans-serif;
    display: flex; align-items: center; justify-content: center;
  }
  .spread {
    width: 1120px; height: 640px; display: flex;
    box-shadow: 0 18px 40px rgba(0,0,0,.25);
  }
  .page {
    position: relative; width: 560px; height: 640px; color: var(--text-light);
    background:
      radial-gradient(ellipse at 60% 40%, rgba(60,60,60,.35), transparent 65%),
      repeating-linear-gradient(45deg, var(--carbon-a) 0 3px, var(--carbon-b) 3px 6px),
      var(--page-black);
  }
  .page--left { border-right: 1px solid #222; }
  .intro { position: absolute; left: 36px; top: 40px; }
  .headline { font-weight: 700; font-size: 20px; line-height: 1.2; white-space: nowrap; }
  .headline--blue { color: var(--accent-blue); }
  .headline--green { color: var(--accent-green); }
  .headline::after {
    content: ""; display: block; width: 100%; height: 1px; margin-top: 6px;
    background: linear-gradient(90deg, #888, transparent);
  }
  .features { list-style: none; font-size: 12.5px; line-height: 1.55; margin: 10px 0 0 12px; }
  .features li::before { content: "• "; }
  .product-photo { position: absolute; border-radius: 6px; }
  .product-name { position: absolute; font-weight: 800; font-size: 18px; line-height: 1.2; }
  .product-name small { display: block; font-weight: 600; font-size: 12px; }
  .product-name--green { color: var(--accent-green); text-transform: uppercase; }
  .spec-table {
    position: absolute; border-collapse: collapse; font-size: 10.5px; color: #111;
    background: var(--cell-light);
  }
  .spec-table th, .spec-table td {
    border: 1px solid var(--cell-line); padding: 3px 6px; text-align: center; line-height: 1.2;
  }
  .spec-table thead th { background: var(--cell-head); color: #fff; font-weight: 700; }
  .spec-table thead th.corner { background: transparent; border: none; }
  .spec-table tbody th {
    text-align: right; font-weight: 700; font-size: 11.5px;
    background: linear-gradient(#fafafa, var(--cell-mid));
  }
  .spec-table td { background: linear-gradient(#ffffff, #dcdcdc); }
  .spec-table .price td { font-weight: 700; }
  .footnotes { position: absolute; list-style: none; font-size: 10px; line-height: 1.5; color: #cfcfcf; }
</style>
</head>
<body>
<main class="spread">
  <section class="page page--left">
    <div class="intro">
      <h2 class="headline headline--blue">World's first Disposable Transmitter</h2>
      <ul class="features">
        <li>Highest and Constant signal strength through entire life</li>
        <li>Buy it for the price you rent</li>
        <li>Lower Financial liability</li>
      </ul>
    </div>
    <div class="product-photo" role="img" aria-label="Disposable transmitter tube with grey end cap"
         style="left:36px;top:170px;width:150px;height:220px;background:linear-gradient(160deg,#6a6a6a,#1b1b1b 45%,#050505);"></div>
    <p class="product-name" style="left:36px;top:410px;">KT-Transmitter – Disposable<small>Norvane Inc. – Patent Pending</small></p>
    <table class="spec-table" style="left:200px;top:200px;width:330px;">
      <thead><tr><th class="corner"></th><th>xSD</th><th>SD</th><th>MD</th></tr></thead>
      <tbody>
        <tr><th>Standard Run-Time¹</th><td>64 hours<br>(2.5 days)</td><td>130 hours<br>(5 days)</td><td>500 hours<br>(21 days)</td></tr>
        <tr><th>Frequency</th><td colspan="3">ELF ~1Hz to 30 Hz (22Hz default)</td></tr>
        <tr><th>Pressure</th><td>1800 PSI</td><td>1800 PSI</td><td>5000 PSI</td></tr>
        <tr><th>Length</th><td>3" (76mm)</td><td>6" (152mm)</td><td>9.5" (241mm)</td></tr>
        <tr><th>Dia</th><td>1" (25.4mm)</td><td>1.25" (32mm)</td><td>1.875" (48mm)</td></tr>
        <tr><th>Temperature²</th><td colspan="3">-40°F to 150°F | -40°C to 65°C</td></tr>
        <tr class="price"><th>Price (USD)</th><td>320</td><td>400</td><td>500</td></tr>
      </tbody>
    </table>
    <ul class="footnotes" style="left:36px;top:510px;">
      <li>1. Standard Run-Time at 25°C. • Continuous option available.</li>
      <li>• Longer Run-Times possible with decreased pulse rate.</li>
      <li>2. Run-Times may vary below 32°F [0°C]</li>
    </ul>
  </section>

  <section class="page page--right">
    <div class="intro">
      <h2 class="headline headline--green">Powerful and Economical<br>in one Package</h2>
      <ul class="features">
        <li>Best signal strength in the industry</li>
        <li>Reliable sealing with spare o-rings</li>
        <li>Includes a Free Harborline style case</li>
      </ul>
    </div>
    <div class="product-photo" role="img" aria-label="Reusable transmitter resting in an open rugged carry case"
         style="left:320px;top:40px;width:210px;height:230px;background:radial-gradient(ellipse at 50% 45%,#5a5a5a,#2a2a2a 55%,#111 85%);"></div>
    <p class="product-name product-name--green" style="left:320px;top:290px;">KT-Transmitter<br>Reusable</p>
    <table class="spec-table" style="left:36px;top:210px;width:260px;">
      <thead><tr><th class="corner"></th><th>xSD</th><th>SD</th><th>MD</th></tr></thead>
      <tbody>
        <tr><th>Standard Run-Time¹</th><td>64 hours<br>(2.5 days)</td><td>130 hours<br>(5 days)</td><td>500 hours<br>(21 days)</td></tr>
        <tr><th>Frequency</th><td colspan="3">ELF ~1Hz to 30 Hz (22Hz default)</td></tr>
        <tr><th>Pressure</th><td>2000 PSI</td><td>2000 PSI</td><td>2000 PSI</td></tr>
        <tr><th>Length</th><td>3.4"<br>(86mm)</td><td>6"<br>(152mm)</td><td>9.5" (241mm)</td></tr>
        <tr><th>Dia</th><td>1"<br>(25.4mm)</td><td>1"<br>(25.4mm)</td><td>1.875" (48mm)</td></tr>
        <tr><th>Temperature²</th><td colspan="3">-40°F to 150°F | -40°C to 65°C</td></tr>
        <tr class="price"><th>Price (USD)</th><td>1200</td><td>1400</td><td>1600</td></tr>
      </tbody>
    </table>
    <ul class="footnotes" style="left:36px;top:510px;">
      <li>• Standard Run-Time at 25°C. • Continuous option available.</li>
      <li>• Longer Run-Times possible with decreased pulse rate.</li>
      <li>• Higher Pressure rating possible • Run-Times may vary below 32°F [0°C]</li>
    </ul>
  </section>
</main>
</body>
</html>
```